Business Card Design Project

Hi I am after a business card double sided 1 side to have the attached PDF on front on the back:

Trent Malloway - Managing Director
Mobile: 0413 268 471
email: trent@vrixo.com.au
web: www.vrixo.com.au

Industry/Entity Type

Business

Font styles to use
Sans Serif

Requirements
Must have
• I want a classy looking card
Nice to have
• I like lime green and black and white

```html
<!DOCTYPE html>
<html lang="en">
<head>
<meta charset="utf-8">
<title>Vrixo Lawns and Gardens – Business Card</title>
<link rel="stylesheet" href="https://fonts.googleapis.com/css2?family=Montserrat:wght@300;400&display=swap">
<style>
  :root {
    --brand-green: #1bb04b;
    --card-white: #ffffff;
    --ink: #333333;
    --backdrop: #ecebe8;
  }
  * { box-sizing: border-box; margin: 0; padding: 0; }
  html, body {
    width: 1200px;
    height: 1000px;
    overflow: hidden;
    background: var(--backdrop);
    font-family: "Montserrat", Arial, sans-serif;
  }
  .stage {
    position: relative;
    width: 1200px;
    height: 1000px;
  }
  .card {
    position: absolute;
    width: 560px;
    height: 340px;
    box-shadow: 0 4px 14px rgba(0, 0, 0, 0.18);
  }
  /* Front */
  .card-front {
    left: 120px;
    top: 150px;
    background: var(--brand-green);
    display: flex;
    align-items: center;
    justify-content: center;
  }
  .brand-lockup {
    display: flex;
    align-items: center;
    gap: 16px;
  }
  .brand-mark {
    width: 52px;
    height: 52px;
    border-radius: 9px;
    background: var(--card-white);
  }
  .brand-name {
    color: var(--card-white);
    font-weight: 300;
    font-size: 26px;
    letter-spacing: 0.3px;
  }
  /* Back */
  .card-back {
    left: 520px;
    top: 500px;
    background: var(--card-white);
    color: var(--ink);
  }
  .back-mark {
    position: absolute;
    left: 40px;
    top: 40px;
    width: 58px;
    height: 58px;
    border-radius: 9px;
    background: var(--brand-green);
  }
  .contact-block {
    position: absolute;
    right: 56px;
    top: 122px;
    text-align: right;
  }
  .person-name {
    font-size: 25px;
    font-weight: 400;
    line-height: 1.1;
  }
  .person-title {
    font-size: 17px;
    font-weight: 300;
    margin-top: 4px;
  }
  .contact-list {
    list-style: none;
    margin-top: 22px;
  }
  .contact-item {
    display: flex;
    justify-content: flex-end;
    align-items: center;
    gap: 10px;
    font-size: 19px;
    font-weight: 300;
    margin-bottom: 6px;
  }
  .contact-icon {
    width: 30px;
    height: 30px;
    border-radius: 5px;
    background: var(--brand-green);
    display: flex;
    align-items: center;
    justify-content: center;
  }
  .web-address {
    position: absolute;
    right: 92px;
    bottom: 30px;
    font-size: 18px;
    font-weight: 300;
  }
</style>
</head>
<body>
<main class="stage">
  <section class="card card-front" aria-label="Card front">
    <div class="brand-lockup">
      <span class="brand-mark" aria-hidden="true"></span>
      <span class="brand-name">Vrixo Lawns and Gardens</span>
    </div>
  </section>

  <section class="card card-back" aria-label="Card back">
    <span class="back-mark" aria-hidden="true"></span>
    <div class="contact-block">
      <h1 class="person-name">Trent Malloway</h1>
      <p class="person-title">Managing Director</p>
      <ul class="contact-list">
        <li class="contact-item">
          <span>0413 268 471</span>
          <span class="contact-icon" aria-label="Mobile">
            <svg width="14" height="20" viewBox="0 0 14 20">
              <rect x="1" y="1" width="12" height="18" rx="2" fill="none" stroke="#fff" stroke-width="1.6"/>
              <rect x="3" y="3.5" width="8" height="11" fill="#fff"/>
              <circle cx="7" cy="16.8" r="1" fill="#fff"/>
            </svg>
          </span>
        </li>
        <li class="contact-item">
          <span>trent@vrixo.com.au</span>
          <span class="contact-icon" aria-label="Email">
            <svg width="20" height="14" viewBox="0 0 20 14">
              <rect x="1" y="1" width="18" height="12" fill="none" stroke="#fff" stroke-width="1.6"/>
              <polyline points="1,1 10,8 19,1" fill="none" stroke="#fff" stroke-width="1.6"/>
            </svg>
          </span>
        </li>
      </ul>
    </div>
    <p class="web-address">www.vrixo.com.au</p>
  </section>
</main>
</body>
</html>
```